Design Contest For Business Cards and PostCards (over-sized/standard)

Type of Contest : Business Card and PostCard Design

Size Requirements : Not 100% sure, whatever size looks best for both business cards and the postcards.

Color Requirements : Include colors from the Logo provided

General Requirements : I will need the template and the formats of both the business card and the postcard at the time of completion and upon receiving payment. Must include logo provided.

Additional Information : I'm a personal trainer that provides fitness instruction and helps clients achieve their goals through exercise and nutrition. Information is below
Business Card:
Company: ORA BOLD WELLNESS
Personal Training|Bootcamp|Kickboxing|Nutrition
Name: Dorian Kettleby
Website: OraBoldWellness.com
Phone: 555.014.2297
Addtl: Somewhere it should say, "Schedule your free session or assessment today" and a quote that says, “Motivation is what gets you started. Habit is what keeps you going.” or "Bold your Fitness"

PostCard (for mailing to potential customers' households)
Company: ORA BOLD WELLNESS
Name: Dorian Kettleby
Phone: 555.014.2297
**Try a free week of Ora Bold Bootcamp**

***The rest of the creativity is up to the designer and i'm looking for double sided on both. I will be using the winning design to upload to either a stampleo or something like it. Thank you.

```html
<!DOCTYPE html>
<html lang="en">
<head>
<meta charset="UTF-8">
<title>Ora Bold Wellness — Business Card</title>
<link rel="stylesheet" href="https://fonts.googleapis.com/css2?family=Open+Sans:ital,wght@0,400;0,600;0,700;0,800;1,600;1,700&display=swap">
<style>
  :root {
    --brand-blue: #1f5ea8;
    --brand-blue-deep: #174a88;
    --brand-blue-light: #3a7cc4;
    --ink: #1d1d1f;
    --paper: #ffffff;
    --swoosh: #eef0f4;
    --backdrop: #e9e6e1;
  }
  * { box-sizing: border-box; margin: 0; padding: 0; }
  html, body {
    width: 1200px; height: 900px; overflow: hidden;
    background: var(--backdrop);
    font-family: "Open Sans", Arial, sans-serif;
  }
  .canvas {
    width: 1200px; height: 900px;
    display: flex; flex-direction: column;
    align-items: center; justify-content: center;
    gap: 50px;
  }
  .card {
    position: relative;
    width: 660px; height: 377px;
    background: var(--paper);
    overflow: hidden;
    box-shadow: 0 6px 18px rgba(0,0,0,.18);
  }
  .card-art { position: absolute; inset: 0; }

  /* Back side */
  .back-quote {
    position: absolute; left: 40px; top: 150px; width: 300px;
    color: var(--paper); font-style: italic; font-weight: 600;
    font-size: 14px; line-height: 1.45;
  }
  .wordmark {
    position: absolute;
    display: flex; align-items: center; gap: 10px;
    color: var(--ink); font-weight: 800; letter-spacing: .5px;
    white-space: nowrap;
  }
  .wordmark-dot {
    width: 18px; height: 18px; border-radius: 50%;
    background: var(--brand-blue);
  }
  .back-wordmark { right: 40px; top: 70px; font-size: 24px; }
  .back-site {
    position: absolute; right: 40px; bottom: 50px;
    color: var(--brand-blue); font-weight: 700; font-size: 15px;
  }

  /* Front side */
  .front-wordmark { right: 40px; top: 58px; font-size: 24px; }
  .trainer-name {
    position: absolute; left: 56px; top: 140px;
    color: var(--brand-blue); font-weight: 700; font-size: 26px;
  }
  .service-list {
    position: absolute; left: 76px; top: 182px;
    color: var(--brand-blue); font-weight: 600; font-size: 14px;
    line-height: 1.45;
  }
  .trainer-phone {
    position: absolute; left: 56px; top: 268px;
    color: var(--brand-blue); font-weight: 600; font-size: 14px;
  }
  .cta-band {
    position: absolute; left: 0; right: 0; bottom: 0; height: 82px;
    background: var(--brand-blue);
    color: var(--paper);
    display: flex; flex-direction: column; align-items: center; justify-content: center;
    padding-left: 180px;
  }
  .cta-slogan { font-weight: 700; font-size: 22px; line-height: 1.2; }
  .cta-offer { font-weight: 700; font-style: italic; font-size: 14px; }
</style>
</head>
<body>
<main class="canvas">

  <section class="card card-back" aria-label="Business card back">
    <svg class="card-art" viewBox="0 0 660 377" aria-hidden="true">
      <defs>
        <radialGradient id="backGlow" cx="35%" cy="50%" r="70%">
          <stop offset="0" stop-color="var(--brand-blue-light)"/>
          <stop offset="1" stop-color="var(--brand-blue-deep)"/>
        </radialGradient>
      </defs>
      <path d="M0 0 H300 C360 110 380 250 430 377 H0 Z" fill="url(#backGlow)"/>
      <path d="M312 0 C372 110 392 250 442 377" fill="none" stroke="var(--brand-blue)" stroke-width="3"/>
    </svg>
    <p class="back-quote">“Motivation is what gets you started.<br>Habit is what keeps you going.”</p>
    <div class="wordmark back-wordmark"><span class="wordmark-dot"></span>ORA BOLD WELLNESS</div>
    <p class="back-site">www.OraBoldWellness.com</p>
  </section>

  <section class="card card-front" aria-label="Business card front">
    <svg class="card-art" viewBox="0 0 660 377" aria-hidden="true">
      <path d="M200 0 C300 120 420 220 660 230 V0 Z" fill="var(--swoosh)"/>
      <path d="M330 0 C400 90 500 150 660 160 V0 Z" fill="#f6f7f9"/>
    </svg>
    <div class="wordmark front-wordmark"><span class="wordmark-dot"></span>ORA BOLD WELLNESS</div>
    <h1 class="trainer-name">Dorian Kettleby</h1>
    <ul class="service-list">
      <li>Personal Training</li>
      <li>Bootcamp</li>
      <li>Kickboxing</li>
      <li>Nutrition</li>
    </ul>
    <p class="trainer-phone">Phone: 555.014.2297</p>
    <div class="cta-band">
      <p class="cta-slogan">"Bold your Fitness"</p>
      <p class="cta-offer">"Schedule your free session or assessment today"</p>
    </div>
  </section>

</main>
</body>
</html>
```